Menopause Bundle Redesign Wordpress site

IMPORTANT: the design will need to look nice on mobile...so please keep that in mind!
We need to redesign our current Wordpress page to make it more appealing and look like an ecommerce page. We need the ability to implement this design on our Wordpress site.
Here is the current page: https://www.rolavexwell.com/supplements/menopause-support-bundle/
However, the reference sample of what it has to look like or complement is also attached.
Attached is the Word document is the copy for the new page and the FAQs text.
The color palette is attached but focus primarily on the SALMON COLOR similar to what is on the current page

Thanks!

Target Market(s)

women in menopause

Industry/Entity Type

health and wellness

Requirements
Must have
• my requirements in word document
Nice to have
• my images in dropbox
Should not have
• NO RANDOM Stock photography of people; use UGC pics in the dropbpx

```html
<!DOCTYPE html>
<html lang="en">
<head>
<meta charset="utf-8">
<title>Menopause Support Bundle</title>
<link rel="stylesheet" href="https://fonts.googleapis.com/css2?family=Montserrat:wght@500;600;700&family=Inter:wght@400;500;600&display=swap">
<style>
:root{
  --salmon:#e5766a;
  --salmon-deep:#d9645a;
  --salmon-soft:#f0b3a8;
  --blush:#f8dcd6;
  --hero-grad-a:#f4c6bc;
  --hero-grad-b:#eda699;
  --panel:#f6f3f2;
  --panel-alt:#fbf9f8;
  --line:#e6dcd9;
  --ink:#1b1b1b;
  --ink-soft:#4d4645;
  --white:#ffffff;
}
*{box-sizing:border-box;margin:0;padding:0}
html,body{width:686px;height:1200px;overflow:hidden;background:var(--panel)}
body{font-family:"Inter",sans-serif;color:var(--ink)}
.page{width:686px;height:1200px;display:grid;grid-template-rows:70px 340px 1fr}

/* nav */
.site-nav{display:flex;align-items:center;gap:26px;padding:0 16px;background:var(--panel-alt);border-bottom:1px solid var(--line)}
.site-nav .brand-dot{width:20px;height:20px;border-radius:50%;border:3px solid var(--salmon);flex:none}
.site-nav ul{display:flex;gap:34px;list-style:none;font-family:"Montserrat",sans-serif;font-size:11px;font-weight:600;letter-spacing:.04em;text-transform:uppercase}
.site-nav li:first-child{color:var(--salmon-deep)}
.nav-cart{margin-left:auto;background:var(--salmon);color:var(--white);font-family:"Montserrat",sans-serif;font-size:11px;font-weight:600;text-transform:uppercase;border-radius:6px;padding:6px 30px}

.btn{display:block;background:var(--salmon);color:var(--white);font-family:"Montserrat",sans-serif;font-weight:700;font-size:12px;text-transform:uppercase;border-radius:8px;text-align:center;box-shadow:0 3px 6px rgba(180,80,70,.25)}
.btn-ghost{background:var(--blush);color:var(--salmon-deep);box-shadow:none;font-size:10px}

/* hero */
.hero{display:grid;grid-template-columns:311px 175px 200px}
.hero-intro{background:linear-gradient(160deg,var(--hero-grad-a),var(--hero-grad-b));padding:36px 0 0 34px;position:relative;border-right:1px solid rgba(255,255,255,.4)}
.hero-intro h1{font-family:"Montserrat",sans-serif;font-weight:600;font-size:36px;line-height:1.12;letter-spacing:-.02em}
.hero-intro .tagline{position:absolute;left:160px;top:150px;width:130px;font-size:10px;line-height:1.5;color:var(--salmon-deep);font-weight:600}
.hero-intro .btn{position:absolute;left:38px;top:222px;width:138px;padding:10px 0}
.hero-detail{background:linear-gradient(170deg,#f2c0b6,#efb0a4);padding:40px 20px 0;border-right:1px solid rgba(255,255,255,.4)}
.hero-detail svg{display:block;margin:0 auto 28px}
.hero-detail p{font-size:10px;line-height:1.55;font-weight:500}
.hero-detail .btn{margin:22px auto 0;width:100px;padding:6px 0}
.hero-offer{background:var(--salmon);display:flex;flex-direction:column;align-items:center;padding-top:26px}
.hero-offer .buy-title{font-family:"Montserrat",sans-serif;font-weight:700;font-size:28px;color:var(--white);margin-top:22px;letter-spacing:-.01em}

/* content grid */
.content{display:grid;grid-template-columns:333px 154px 199px;background:var(--panel-alt)}
.col{display:grid;border-right:1px solid var(--line)}
.col:last-child{border-right:0}
.col-main{grid-template-rows:475px 1fr}
.col-mid,.col-side{grid-template-rows:232px 262px 1fr}
.cell{border-bottom:1px solid var(--line);padding:22px 14px;text-align:center}
.cell:last-child{border-bottom:0}
h2{font-family:"Montserrat",sans-serif;font-weight:600;font-size:20px;letter-spacing:-.01em;text-transform:uppercase;line-height:1.2}
.cell p{font-size:10px;line-height:1.6;font-weight:500;color:var(--ink-soft);margin-top:12px;text-align:left}
.cell .lead{text-align:center;margin-top:6px}

.intro-cell{padding:30px 26px 0 30px;border-bottom:1px solid var(--line)}
.intro-cell h2{text-transform:none;font-size:26px;font-weight:500}
.intro-cell p{font-size:11px;line-height:1.5;font-weight:500;color:var(--salmon-deep);margin-top:8px}
.product-shot{margin-top:26px;height:330px;border-radius:12px;background:linear-gradient(150deg,#f6ddd7 0%,#ee a89c 100%);background:linear-gradient(150deg,#f6ddd7 0%,#eda89c 100%)}

.faq-main{display:grid;grid-template-columns:190px 1fr;padding:0;text-align:left}
.faq-main .faq-text{padding:22px 14px 0 26px;border-right:1px solid var(--line);display:flex;flex-direction:column}
.faq-main .btn{margin-top:auto;margin-bottom:26px;padding:10px 0}
.icon-grid{display:grid;grid-template-columns:1fr 1fr;align-content:center;row-gap:18px;padding:18px 8px}
.icon-grid figure{display:flex;flex-direction:column;align-items:center;gap:5px}
.icon-grid figcaption{font-size:9px;font-weight:600;color:var(--salmon-deep)}

.faq-cell .btn{margin-top:16px;width:100%;padding:8px 0}
.icon-row{display:flex;justify-content:center;gap:16px;margin-top:22px}
.dots{display:flex;justify-content:center;gap:8px;margin-top:18px}
.center-icon{display:block;margin:20px auto 0}
</style>
</head>
<body>
<svg width="0" height="0" style="position:absolute">
  <defs>
    <radialGradient id="orb" cx="40%" cy="35%" r="70%">
      <stop offset="0" stop-color="#f2a095"/>
      <stop offset="1" stop-color="#d95d52"/>
    </radialGradient>
    <symbol id="orb-base" viewBox="0 0 60 60">
      <circle cx="30" cy="30" r="28" fill="#f6d8d2"/>
      <circle cx="30" cy="30" r="24" fill="url(#orb)"/>
    </symbol>
    <symbol id="ico-ring" viewBox="0 0 60 60"><use href="#orb-base"/><circle cx="30" cy="30" r="9" fill="none" stroke="#fbe3de" stroke-width="2.5"/></symbol>
    <symbol id="ico-tick" viewBox="0 0 60 60"><use href="#orb-base"/><path d="M21 31l6 6 12-14" fill="none" stroke="#fff" stroke-width="3" stroke-linecap="round" stroke-linejoin="round"/></symbol>
    <symbol id="ico-moon" viewBox="0 0 60 60"><use href="#orb-base"/><path d="M34 20a11 11 0 1 0 6 18 9 9 0 0 1-6-18z" fill="#fff"/></symbol>
    <symbol id="ico-sun" viewBox="0 0 60 60"><use href="#orb-base"/><circle cx="30" cy="30" r="6" fill="#fff"/><path d="M30 17v4M30 39v4M17 30h4M39 30h4M21 21l3 3M36 36l3 3M39 21l-3 3M24 36l-3 3" stroke="#fff" stroke-width="2.2" stroke-linecap="round"/></symbol>
    <symbol id="ico-heart" viewBox="0 0 60 60"><use href="#orb-base"/><path d="M30 40s-11-6.5-11-13.5A5.8 5.8 0 0 1 30 23a5.8 5.8 0 0 1 11 3.5C41 33.5 30 40 30 40z" fill="#fff"/></symbol>
    <symbol id="ico-bolt" viewBox="0 0 60 60"><use href="#orb-base"/><path d="M32 17l-10 15h8l-2 11 10-15h-8z" fill="#fff"/></symbol>
    <symbol id="ico-drop" viewBox="0 0 60 60"><use href="#orb-base"/><path d="M30 18c-5 7-8 11-8 15a8 8 0 0 0 16 0c0-4-3-8-8-15z" fill="#fff"/></symbol>
    <symbol id="ico-plus" viewBox="0 0 60 60"><use href="#orb-base"/><path d="M30 21v18M21 30h18" stroke="#fff" stroke-width="3" stroke-linecap="round"/></symbol>
    <symbol id="ico-arrow" viewBox="0 0 60 60"><use href="#orb-base"/><path d="M21 30h17M32 23l7 7-7 7" fill="none" stroke="#fff" stroke-width="3" stroke-linecap="round" stroke-linejoin="round"/></symbol>
  </defs>
</svg>

<div class="page">
  <nav class="site-nav">
    <span class="brand-dot"></span>
    <ul>
      <li>Shop Support</li>
      <li>About</li>
      <li>Reviews</li>
      <li>Ingredients</li>
    </ul>
    <span class="nav-cart">Cart</span>
  </nav>

  <header class="hero">
    <div class="hero-intro">
      <h1>Menopause<br>Support</h1>
      <p class="tagline">Daily relief for hot flashes, sleep and mood</p>
      <span class="btn">Shop Bundle</span>
    </div>
    <div class="hero-detail">
      <svg width="64" height="64"><use href="#ico-ring"/></svg>
      <p>Natural herbs blended to ease your changing body every day.</p>
      <span class="btn btn-ghost">Learn More</span>
    </div>
    <div class="hero-offer">
      <svg width="130" height="130" viewBox="0 0 130 130">
        <circle cx="65" cy="65" r="62" fill="#f3c1b8"/>
        <circle cx="65" cy="65" r="54" fill="#e0685d"/>
        <circle cx="65" cy="65" r="46" fill="#fbeae6"/>
        <path d="M44 60h36l-4 20H48z" fill="none" stroke="#e0685d" stroke-width="4" stroke-linejoin="round"/>
        <path d="M54 60v-6a8 8 0 0 1 16 0v6" fill="none" stroke="#e0685d" stroke-width="4"/>
      </svg>
      <span class="buy-title">BUY NOW</span>
    </div>
  </header>

  <main class="content">
    <section class="col col-main">
      <div class="intro-cell">
        <h2>Menopause</h2>
        <p>Gentle support made for every stage of change.</p>
        <div class="product-shot" role="img" aria-label="Menopause support supplement bottle with coral leaves and a capsule"></div>
      </div>
      <div class="cell faq-main">
        <div class="faq-text">
          <h2>FAQ</h2>
          <p>How soon will I notice results? Most women feel a change within two to four weeks.</p>
          <span class="btn">Buy Now</span>
        </div>
        <div class="icon-grid">
          <figure><svg width="38" height="38"><use href="#ico-drop"/></svg><figcaption>Hot flashes</figcaption></figure>
          <figure><svg width="38" height="38"><use href="#ico-moon"/></svg><figcaption>Sleep</figcaption></figure>
          <figure><svg width="38" height="38"><use href="#ico-heart"/></svg><figcaption>Mood</figcaption></figure>
          <figure><svg width="38" height="38"><use href="#ico-bolt"/></svg><figcaption>Energy</figcaption></figure>
          <figure><svg width="38" height="38"><use href="#ico-sun"/></svg><figcaption>Focus</figcaption></figure>
          <figure><svg width="38" height="38"><use href="#ico-plus"/></svg><figcaption>Skin</figcaption></figure>
        </div>
      </div>
    </section>

    <section class="col col-mid">
      <div class="cell">
        <h2>Benefits</h2>
        <p>Cools hot flashes and supports calm, restful nights so you wake refreshed.</p>
      </div>
      <div class="cell">
        <svg width="70" height="70" viewBox="0 0 70 70" style="margin-top:8px">
          <rect x="4" y="4" width="62" height="62" rx="6" fill="#e67a6e"/>
          <path d="M23 36l8 8 16-18" fill="none" stroke="#fff" stroke-width="3.5" stroke-linecap="round" stroke-linejoin="round"/>
        </svg>
        <p style="margin-top:30px">Plant-based formula with no fillers, tested for purity.</p>
      </div>
      <div class="cell faq-cell">
        <h2>FAQ</h2>
        <p>Can I take it with other vitamins? Yes, it pairs well.</p>
        <svg class="center-icon" width="80" height="80"><use href="#ico-tick"/></svg>
      </div>
    </section>

    <section class="col col-side">
      <div class="cell">
        <h2>How It Helps</h2>
        <p>Balances mood, eases night sweats and helps you feel like yourself again each day.</p>
      </div>
      <div class="cell">
        <h2>Results</h2>
        <p class="lead">Energy, focus and comfort</p>
        <div class="icon-row">
          <svg width="72" height="72"><use href="#ico-bolt"/></svg>
          <svg width="72" height="72"><use href="#ico-sun"/></svg>
        </div>
      </div>
      <div class="cell faq-cell">
        <h2>Dosage</h2>
        <p>Is it safe daily? Yes, take two capsules with food.</p>
        <div class="dots">
          <svg width="34" height="34"><use href="#ico-tick"/></svg>
          <svg width="34" height="34"><use href="#ico-moon"/></svg>
          <svg width="34" height="34"><use href="#ico-heart"/></svg>
          <svg width="34" height="34"><use href="#ico-arrow"/></svg>
        </div>
        <span class="btn">Buy Now</span>
      </div>
    </section>
  </main>
</div>
</body>
</html>
```